Vitalquorra.com

I need a web design for a Online Wellness Center based in Chicago, IL and it's called "Vitalquorra" We provide Health risk assessment to individuals and interventions. Our portal has a Health Activity tracker where our members record health activities and aerobic miles and biometric data. Our Online wellness center tracks the participant's progress toward health goals and awards points for completed activities.
I started working on this website but the designer was not able to designer a website which describes what we do. I need a fresh look on this project. I need a very attractive, responsive website which says what we do.
These are the things we do.
1. We provide Health Risk Assessments to individuals and Co-operations
2. We Provide Free health screenings to undeserved communities
3. Assist individuals access free or affordable medications
4. We ask providers/doctors to see (or do a complete physical) one individual free of charge once a year (those individuals who are no insured and don't have money to pay from their pocket)
5. Assist patient access lab work at low cost
Our goal is to provide services that will lower the cost of care for our members.

Here is the website: www.vitalquorra.com still underdevelopment. PLEASE DO NOT COPY THIS STYLE OF WEBSITE. IT'S A BAD DESIGN AND THAT IS WHY I'M RE-DESIGNING THE SITE

Target Market(s)

Health individuals between the age of 21 to 65 Plus years old. Insured and uninsured

Industry/Entity Type

Health And Wellness

Coding

Coded - Design and coding required

Number of Pages Required

5+ page

Colors
0292cd

Requirements
Must have
• I'm still working on this websiteHere is the menu: Home, About us, Services, Health Screening, Providers, Contacts
• Please see. www.vitalquorra.com
Nice to have
• Event calender
• Upcoming Event
• Medication
• Lab assist
• Providers/Free Clinics

```html
<!DOCTYPE html>
<html lang="en">
<head>
<meta charset="utf-8">
<title>Vitalquorra – Online Wellness Center</title>
<link href="https://fonts.googleapis.com/css2?family=Oswald:wght@400;500;600&family=Open+Sans:wght@400;600;700&display=swap" rel="stylesheet">
<style>
:root{
  --navy:#1a2f7a;
  --navy-dark:#142463;
  --blue:#0292cd;
  --green:#7cc242;
  --green-dark:#5fa52a;
  --ink:#1f2d5c;
  --text:#555b66;
  --light:#eef1f5;
  --white:#ffffff;
}
*{box-sizing:border-box;margin:0;padding:0}
html,body{width:758px;height:1200px;overflow:hidden}
body{position:relative;background:var(--white);font-family:"Open Sans",sans-serif;color:var(--text);font-size:7px;line-height:1.45}
.abs{position:absolute}
.head-band{left:0;top:0;width:758px;height:250px;background:radial-gradient(ellipse at 30% 40%,#22398c 0%,var(--navy) 50%,var(--navy-dark) 100%)}
.logo{left:96px;top:16px;display:flex;align-items:center;gap:7px;color:var(--white);font-weight:700;font-size:19px;letter-spacing:-.3px}
.logo i{width:18px;height:18px;border-radius:50%;background:var(--green);display:block}
.top-contact{right:96px;top:14px;color:var(--white);font-size:7.5px;line-height:1.8;text-align:right}
.top-contact span{display:flex;align-items:center;gap:4px;justify-content:flex-end}
.nav{left:96px;top:56px;width:566px;height:28px;background:var(--navy-dark);display:flex}
.nav a{color:var(--white);text-decoration:none;font-family:"Oswald",sans-serif;font-size:9px;letter-spacing:.4px;padding:0 17px;line-height:28px}
.nav a.active{background:var(--green)}
.hero{left:96px;top:84px;width:566px;height:270px;background:linear-gradient(90deg,#f4f6f9 0%,#e6eaf0 100%);overflow:hidden}
.hero-photo{position:absolute;right:0;top:0;width:250px;height:270px;background:linear-gradient(160deg,#d9dfe7 0%,#c7d0dc 55%,#e4e8ee 100%)}
.hero h1{position:absolute;left:24px;top:30px;font-family:"Oswald",sans-serif;font-weight:600;font-size:31px;line-height:1.08;color:var(--ink);letter-spacing:.3px}
.hero .tag{position:absolute;left:24px;top:112px;width:290px;height:24px;background:var(--navy);color:var(--white);font-family:"Oswald",sans-serif;font-size:11px;line-height:24px;padding-left:10px;letter-spacing:.3px}
.hero p{position:absolute;left:24px;top:145px;width:280px;font-size:7.5px;color:var(--text)}
.btn{background:var(--green);color:var(--white);font-family:"Oswald",sans-serif;font-size:9px;letter-spacing:.4px;text-align:center}
.hero .btn{position:absolute;left:24px;top:192px;width:62px;height:20px;line-height:20px}
h2.title{font-family:"Oswald",sans-serif;font-weight:500;font-size:12px;color:var(--ink);letter-spacing:.3px}
h2.title b{color:var(--blue);font-weight:500}
.welcome{left:96px;top:374px;width:320px}
.welcome p{margin-top:6px}
.events-bar{left:96px;top:470px;width:320px;height:16px;background:var(--navy);color:var(--white);font-family:"Oswald",sans-serif;font-size:9px;line-height:16px;padding-left:8px}
.events-bar b{color:var(--green);font-weight:500}
.events-bar em{position:absolute;right:0;top:0;height:16px;width:30px;background:var(--green);font-style:normal;text-align:center;font-size:7px}
.event{left:96px;width:320px;height:42px;display:flex;gap:8px;border-bottom:1px solid #e2e5ea}
.date{width:26px;height:34px;background:var(--navy);color:var(--white);text-align:center;font-family:"Oswald",sans-serif;font-size:11px;line-height:1;padding-top:4px}
.date small{display:block;font-size:6px;margin-top:2px}
.event h3{font-family:"Oswald",sans-serif;font-weight:500;font-size:8px;color:var(--blue)}
.event p{font-size:6.3px;line-height:1.4}
.more{left:370px;top:630px;width:46px;height:12px;line-height:12px;background:var(--navy);color:var(--white);font-size:6px;text-align:center}
.cal{left:432px;top:374px;width:230px}
.cal h4,.benefits h4{background:var(--navy);color:var(--white);font-family:"Oswald",sans-serif;font-weight:400;font-size:8.5px;height:16px;line-height:16px;padding-left:8px}
.cal .month{background:var(--green);color:var(--white);text-align:center;font-size:7px;font-weight:700;height:14px;line-height:14px;margin-top:2px}
.grid{display:grid;grid-template-columns:repeat(7,1fr);gap:1px;background:var(--blue);padding:1px;font-size:6.5px;text-align:center}
.grid span{background:var(--white);height:13px;line-height:13px;color:var(--ink)}
.grid .wd{background:var(--blue);color:var(--white);font-weight:700}
.grid .em{background:#d9ecf7}
.grid .hl{background:var(--green);color:var(--white)}
.benefits{left:432px;top:522px;width:230px;height:124px;background:linear-gradient(180deg,#1f74c4 0%,var(--blue) 100%)}
.benefits ul{list-style:none;padding:6px 10px;color:var(--white);font-size:7px;line-height:13px}
.benefits li::before{content:"›";color:var(--green);font-weight:700;margin-right:5px}
.services-title{left:96px;top:776px}
.card{top:800px;width:134px}
.card .photo{height:72px;background:linear-gradient(135deg,#cfe3ef,#9fbfd6)}
.card .icon{position:absolute;left:12px;top:60px;width:24px;height:24px;border-radius:50%;background:var(--blue);border:2px solid var(--white);display:flex;align-items:center;justify-content:center}
.card h3{margin-top:16px;font-family:"Oswald",sans-serif;font-weight:500;font-size:9px;color:var(--ink)}
.card p{font-size:6.3px;margin-top:3px}
.footer{left:0;top:1018px;width:758px;height:156px;background:var(--navy)}
.foot-title{font-family:"Oswald",sans-serif;font-size:10px;color:var(--white);letter-spacing:.3px}
.form{left:96px;top:1032px;width:300px}
.field{background:var(--white);height:16px;font-size:6.5px;line-height:16px;padding-left:6px;color:#9aa1ac}
.form .row{display:flex;gap:6px;margin-top:10px}
.form .row .field{flex:1}
.form .msg{display:flex;gap:6px;margin-top:6px}
.form .msg .field{flex:1;height:44px}
.form .btn{width:40px;height:44px;line-height:44px}
.visit{left:470px;top:1032px;width:192px;color:#c9d3ee;font-size:7px}
.visit div{display:flex;gap:6px;margin-top:9px;align-items:flex-start}
.bottom{left:0;top:1174px;width:758px;height:26px;background:var(--light);font-size:6.5px;line-height:26px}
.bottom .links{position:absolute;left:96px}
.bottom .copy{position:absolute;right:96px}
</style>
</head>
<body>
<div class="abs head-band"></div>

<div class="abs logo"><i></i>Vitalquorra</div>
<div class="abs top-contact">
  <span><svg width="7" height="7" viewBox="0 0 10 10"><path d="M2 1l2 2-1 1.5c.8 1.4 1.6 2.2 3 3L7.5 6l2 2-1.5 1.5C4.5 9 1 5.5.5 2.5z" fill="#7cc242"/></svg>(312) 555-0148</span>
  <span><svg width="8" height="6" viewBox="0 0 10 7"><rect x=".5" y=".5" width="9" height="6" fill="none" stroke="#7cc242"/><path d="M.5.5L5 4 9.5.5" fill="none" stroke="#7cc242"/></svg>info@vitalquorra.com</span>
</div>

<nav class="abs nav">
  <a class="active">HOME</a><a>ABOUT US</a><a>SERVICES</a><a>HEALTH SCREENING</a><a>PROVIDERS</a><a>CONTACTS</a>
</nav>

<section class="abs hero">
  <div class="hero-photo" role="img" aria-label="Smiling doctor in a white coat with a stethoscope"></div>
  <h1>DID YOU HOW ABOUT<br>YOUR RISK FACTOR</h1>
  <div class="tag">WE AVAILS HEALTH SCREENING SERVICES</div>
  <p>A lot of cardiovascular doctors support preventive health screenings for cardiovascular disease and patients with key risk factors.</p>
  <div class="btn">READ MORE</div>
</section>

<section class="abs welcome">
  <h2 class="title">WELCOME TO <b>VITALQUORRA</b></h2>
  <p>Vitalquorra is an online wellness center whose key objective is to make the growth in heart rate and everyday effort visible and help members reach their goals. Our portal keeps records of health activities, aerobic miles and biometric data, and it awards points for each completed activity. We provide health risk assessments to individuals and companies, free health screenings to underserved communities, and help people reach affordable medication and low cost lab work.</p>
</section>

<div class="abs events-bar">UPCOMING <b>EVENT</b><em>VIEW</em></div>
<div class="abs event" style="top:492px"><div class="date">13<small>SEP 2016</small></div><div><h3>LOREM IPSUM DOLOR SIT AMET, CONSECTETUR</h3><p>Free community blood pressure and glucose screening with our partner nurses, open to all members and walk in guests without any appointment needed.</p></div></div>
<div class="abs event" style="top:538px"><div class="date">17<small>SEP 2016</small></div><div><h3>VESTIBULUM ELIT. VIVAMUS UT NEQUE FELIS</h3><p>Group walk and aerobic miles challenge along the lakefront, with points awarded to every participant who records the activity in the tracker.</p></div></div>
<div class="abs event" style="top:584px"><div class="date">24<small>SEP 2016</small></div><div><h3>PHASELLUS NIBUS NUNC UT LACUS RUTRUM CONVALLIS</h3><p>Open clinic day where volunteer providers offer one complete physical free of charge to uninsured members who registered in advance online.</p></div></div>
<div class="abs more">View more ›</div>

<aside class="abs cal">
  <h4>VITALQUORRA CALENDER</h4>
  <div class="month">SEPTEMBER 2016</div>
  <div class="grid">
    <span class="wd">S</span><span class="wd">M</span><span class="wd">T</span><span class="wd">W</span><span class="wd">T</span><span class="wd">F</span><span class="wd">S</span>
    <span class="em"></span><span class="em"></span><span class="em"></span><span class="em"></span><span>1</span><span>2</span><span>3</span>
    <span>4</span><span>5</span><span>6</span><span>7</span><span>8</span><span>9</span><span>10</span>
    <span>11</span><span>12</span><span class="hl">13</span><span>14</span><span>15</span><span>16</span><span class="hl">17</span>
    <span>18</span><span>19</span><span>20</span><span>21</span><span>22</span><span>23</span><span class="hl">24</span>
    <span>25</span><span>26</span><span>27</span><span>28</span><span>29</span><span>30</span><span class="em"></span>
  </div>
</aside>

<aside class="abs benefits">
  <h4>BENEFITS OF WELLNESS SERVICES</h4>
  <ul>
    <li>Free medication access</li>
    <li>Health Risk Assessment</li>
    <li>Free health screenings</li>
    <li>Affordable lab work</li>
    <li>Yearly free physical</li>
    <li>Health activity tracker</li>
    <li>Points for healthy goals</li>
  </ul>
</aside>

<h2 class="abs title services-title">OUR BEST <b>SERVICES</b></h2>

<div class="abs card" style="left:96px">
  <div class="photo" role="img" aria-label="Pharmacist handing medication to a patient"></div>
  <div class="icon"><svg width="12" height="12" viewBox="0 0 12 12"><path d="M5 2h2v3h3v2H7v3H5V7H2V5h3z" fill="#fff"/></svg></div>
  <h3>MEDICATION</h3>
  <p>One of our Certified Patient Advocates helps members get free or affordable medication.</p>
</div>
<div class="abs card" style="left:240px">
  <div class="photo" role="img" aria-label="Doctor examining a patient"></div>
  <div class="icon"><svg width="12" height="12" viewBox="0 0 12 12"><path d="M5 2h2v3h3v2H7v3H5V7H2V5h3z" fill="#fff"/></svg></div>
  <h3>PROVIDERS</h3>
  <p>We ask providers to see one uninsured person free of charge once a year.</p>
</div>
<div class="abs card" style="left:384px">
  <div class="photo" role="img" aria-label="Laboratory technician with test tubes"></div>
  <div class="icon"><svg width="12" height="12" viewBox="0 0 12 12"><path d="M5 2h2v3h3v2H7v3H5V7H2V5h3z" fill="#fff"/></svg></div>
  <h3>LAB TEST</h3>
  <p>We help patients reach lab work at a low cost near the place they live.</p>
</div>
<div class="abs card" style="left:528px">
  <div class="photo" role="img" aria-label="Community free clinic waiting room"></div>
  <div class="icon"><svg width="12" height="12" viewBox="0 0 12 12"><path d="M5 2h2v3h3v2H7v3H5V7H2V5h3z" fill="#fff"/></svg></div>
  <h3>FREE CLINICS</h3>
  <p>We list free clinics and screenings for underserved communities in Chicago.</p>
</div>

<footer class="abs footer"></footer>
<div class="abs form">
  <div class="foot-title">CONTACT US</div>
  <div class="row"><div class="field">Name</div><div class="field">Email</div></div>
  <div class="msg"><div class="field">Comments</div><div class="btn">SUBMIT</div></div>
</div>
<div class="abs visit">
  <div class="foot-title">VISIT TO VITALQUORRA</div>
  <div><svg width="8" height="10" viewBox="0 0 8 10"><path d="M4 0a4 4 0 014 4c0 3-4 6-4 6S0 7 0 4a4 4 0 014-4z" fill="#7cc242"/><circle cx="4" cy="4" r="1.4" fill="#1a2f7a"/></svg><span>4020 Lakeview Street,<br>Chicago, IL 60611</span></div>
  <div><svg width="8" height="8" viewBox="0 0 10 10"><path d="M2 1l2 2-1 1.5c.8 1.4 1.6 2.2 3 3L7.5 6l2 2-1.5 1.5C4.5 9 1 5.5.5 2.5z" fill="#7cc242"/></svg><span>(312) 555-0148</span></div>
  <div><svg width="8" height="6" viewBox="0 0 10 7"><rect x=".5" y=".5" width="9" height="6" fill="none" stroke="#7cc242"/><path d="M.5.5L5 4 9.5.5" fill="none" stroke="#7cc242"/></svg><span>info@vitalquorra.com</span></div>
</div>

<div class="abs bottom">
  <span class="links">Home &nbsp;|&nbsp; About us &nbsp;|&nbsp; Services &nbsp;|&nbsp; Health Screening &nbsp;|&nbsp; Providers &nbsp;|&nbsp; Contacts</span>
  <span class="copy">© 2016 Vitalquorra. Privacy Policy | Terms of Use</span>
</div>
</body>
</html>
```